Brava Helix Inc - Cutting-Edge Biotech Laboratory - Sleek & Sophisticated

Please design a website that has more of a high-tech and high-end feel, with contents outlined in the uploaded file.

Please have main tabs of the following categories: Home, About, FDA & LAWS, Science, Products, Media, Contact.

Media can include all the videos and photos.

Current website: www.bravahelixlabs.example - it needs to be much more high-end, sleek and more organized. Please do NOT follow the outlines in the old website, but follow the uploaded CONTENT file.

Target Market(s)

doctors

Industry/Entity Type

Biotechnology

Coding

Coded - Design and coding required

Number of Pages Required

5+ page

Requirements
Must have
• Logo
Nice to have
• Some lotion on the website

```html
<!DOCTYPE html>
<html lang="en">
<head>
<meta charset="utf-8">
<title>Brava Helix Inc</title>
<link href="https://fonts.googleapis.com/css2?family=Roboto:wght@300;400;500&display=swap" rel="stylesheet">
<style>
  :root {
    --brand-blue: #0a74c9;
    --hero-deep: #03070f;
    --hero-mid: #0b1f3c;
    --hero-band: #1f4f86;
    --hero-glow: #7fb3e6;
    --white: #ffffff;
    --ink: #2b3550;
    --label: #7f8fb0;
    --body: #5b6478;
    --photo-light: #eceff1;
    --photo-mid: #c6ccd2;
  }
  * { box-sizing: border-box; margin: 0; padding: 0; }
  html, body {
    width: 1200px; height: 676px; overflow: hidden;
    background: var(--white);
    font-family: "Roboto", "Helvetica Neue", Arial, sans-serif;
  }
  .page { position: relative; width: 1200px; height: 676px; overflow: hidden; }

  .hero {
    position: absolute; left: 0; top: 0; width: 1200px; height: 492px;
    background:
      radial-gradient(ellipse 260px 70px at 1060px 250px, rgba(127,179,230,0.55), transparent 75%),
      radial-gradient(ellipse 300px 80px at 760px 340px, rgba(127,179,230,0.45), transparent 75%),
      radial-gradient(ellipse 280px 70px at 420px 420px, rgba(127,179,230,0.35), transparent 75%),
      radial-gradient(ellipse 200px 50px at 120px 470px, rgba(127,179,230,0.3), transparent 75%),
      linear-gradient(163deg,
        transparent 0%, transparent 40%,
        rgba(31,79,134,0.55) 50%, rgba(63,120,180,0.75) 57%,
        rgba(31,79,134,0.6) 66%, transparent 78%),
      linear-gradient(175deg, var(--hero-deep) 0%, #071329 45%, var(--hero-mid) 100%);
  }

  .brand {
    position: absolute; left: 44px; top: 0; width: 168px; height: 150px;
    background: var(--brand-blue);
    clip-path: polygon(0 0, 100% 0, 100% 100%, 6% 84%);
    display: flex; flex-direction: column; align-items: center; justify-content: center;
    gap: 12px; padding-bottom: 18px;
  }
  .brand-dot { width: 30px; height: 30px; border-radius: 50%; background: var(--white); }
  .brand-name { color: var(--white); font-size: 17px; font-weight: 400; letter-spacing: 0.5px; }

  .main-nav { position: absolute; left: 428px; top: 36px; display: flex; gap: 28px; }
  .main-nav a { color: var(--white); text-decoration: none; font-size: 14px; font-weight: 500; }

  .header-actions { position: absolute; right: 30px; top: 28px; display: flex; gap: 8px; }
  .btn {
    height: 32px; padding: 0 11px; border-radius: 16px; font-size: 12.5px;
    display: flex; align-items: center; text-decoration: none; font-weight: 400;
  }
  .btn-outline { color: var(--white); border: 1.5px solid var(--white); }
  .btn-solid { color: #111; background: var(--white); }

  .about { position: absolute; left: 0; top: 492px; width: 1200px; height: 184px; background: var(--white); }
  .about-label { position: absolute; left: 54px; top: 40px; color: var(--label); font-size: 16px; font-weight: 300; }
  .about-title { position: absolute; left: 54px; top: 62px; color: var(--ink); font-size: 29px; font-weight: 400; }
  .about-text {
    position: absolute; left: 56px; top: 122px; width: 540px;
    color: var(--body); font-size: 13px; line-height: 20px; font-weight: 300;
  }
  .about-text p + p { margin-top: 14px; }
  .about-photo {
    position: absolute; left: 712px; top: 70px; width: 400px; height: 130px;
    background: linear-gradient(100deg, var(--photo-mid), var(--photo-light) 55%, #dde2e6);
  }
</style>
</head>
<body>
<div class="page">
  <section class="hero" role="img" aria-label="Glowing blue network of connected points sweeping diagonally across a dark navy background"></section>

  <header>
    <div class="brand">
      <span class="brand-dot"></span>
      <span class="brand-name">BRAVA HELIX</span>
    </div>
    <nav class="main-nav">
      <a href="#">About Us</a>
      <a href="#">Our Products</a>
      <a href="#">FDA &amp; LAWS</a>
      <a href="#">Science</a>
    </nav>
    <div class="header-actions">
      <a class="btn btn-outline" href="#">Contact Us</a>
      <a class="btn btn-solid" href="#">Physician's Login</a>
    </div>
  </header>

  <section class="about">
    <div class="about-label">About Us</div>
    <h1 class="about-title">Who we are ?</h1>
    <div class="about-text">
      <p>Brava Helix Cell Shot Therapy provides Embryonic Stem Cells and unique protocols to doctors in order to help their patients who face major health conditions as well as individuals who simply wish to stay young and healthy.</p>
      <p>Over the past five years of development, we have successfully conducted research into</p>
    </div>
    <div class="about-photo" role="img" aria-label="Photo of a team of doctors in a bright clinic meeting"></div>
  </section>
</div>
</body>
</html>
```